Design a 4-page brochure for Juniper Ridge Fund

Please use the content from the Updated Brochure attachment to design a 4-page 4-color glossy letter sized brochure for Juniper Ridge Fund. The content and concept of the brochure are in the attached word document. Additional photos are attached, and a logo for the fund will be forthcoming (the logo is currently a contest on ArtHive)
We own the attached photos that can be used in brochure.

Target Market(s)

Investors

Industry/Entity Type

Investment

```html
<!DOCTYPE html>
<html lang="en">
<head>
<meta charset="utf-8">
<title>Juniper Ridge Fund – Brochure Spread</title>
<link rel="stylesheet" href="https://fonts.googleapis.com/css2?family=Lato:ital,wght@0,300;0,400;0,700;1,400&family=Open+Sans:wght@400;600;700&display=swap">
<style>
  :root {
    --brand-blue: #4a90d0;
    --brand-blue-deep: #2f6fb3;
    --title-blue: #3d86c6;
    --corner-blue: #27579a;
    --paper: #ffffff;
    --paper-shade: #f3f4f6;
    --text: #5f6368;
    --text-strong: #2e3135;
    --row-tint: #e6e6f3;
    --grid: #c9cbe0;
    --backdrop: #dcdcd8;
  }
  * { box-sizing: border-box; margin: 0; padding: 0; }
  html, body { width: 1200px; height: 804px; overflow: hidden; background: var(--backdrop); }
  .spread { position: relative; width: 1200px; height: 804px; display: flex; }
  .page { position: relative; width: 600px; height: 804px; background: var(--paper); overflow: hidden; }
  .page--left { box-shadow: inset -18px 0 24px -18px rgba(0,0,0,.25); }
  .page--right { box-shadow: inset 18px 0 24px -18px rgba(0,0,0,.25); }

  .photo { position: absolute; }
  .photo--handshake { left: 0; top: 0; width: 600px; height: 250px;
    background: linear-gradient(135deg, #c9d3de 0%, #7f8fa3 45%, #38424f 100%); }
  .photo--cash { left: 60px; top: 520px; width: 480px; height: 140px;
    background: linear-gradient(180deg, #c8cfbf 0%, #8e9a83 60%, #6e7a66 100%); }
  .photo--couple { left: 0; top: 0; width: 255px; height: 190px;
    background: linear-gradient(160deg, #e3ddd2 0%, #b9a996 50%, #5f7f86 100%); }
  .photo--estate { left: 260px; top: 0; width: 340px; height: 190px;
    background: linear-gradient(180deg, #cfe0ee 0%, #b6aa95 55%, #5d7c45 100%); }
  .photo--boardroom { left: 60px; top: 508px; width: 480px; height: 130px; border-radius: 10px;
    background: linear-gradient(180deg, #e4ddd0 0%, #b8a488 55%, #5a4536 100%); }

  .wave { position: absolute; left: 0; width: 600px; }
  .wave--top { top: 0; height: 300px; }
  .wave--bottom { bottom: 0; height: 140px; }

  .body-copy { position: absolute; left: 62px; top: 292px; width: 476px;
    font-family: "Lato", sans-serif; font-weight: 300; font-size: 10.5px; line-height: 1.55; color: var(--text); }
  .body-copy p { margin-bottom: 11px; }
  .body-copy .lead { font-weight: 700; color: var(--text-strong); }

  .brand { position: absolute; left: 0; width: 600px; top: 716px; text-align: center; color: #fff;
    font-family: "Lato", sans-serif; }
  .brand__mark { display: inline-flex; align-items: center; gap: 8px; font-size: 15px; font-weight: 400; letter-spacing: .5px; }
  .brand__square { width: 16px; height: 16px; border: 2px solid #fff; }
  .brand__url { margin-top: 14px; font-size: 12px; letter-spacing: 3px; }

  .pro-forma { position: absolute; left: 0; width: 600px; top: 200px; text-align: center;
    font-family: "Open Sans", sans-serif; font-size: 28px; font-weight: 400; color: var(--title-blue); letter-spacing: .5px; }

  .scenario { position: absolute; left: 48px; width: 504px; }
  .scenario--two { top: 248px; }
  .scenario--four { top: 360px; }
  .scenario__title { position: relative; background: var(--brand-blue); color: #fff; text-align: center;
    font-family: "Open Sans", sans-serif; font-weight: 600; font-size: 14px; height: 22px; line-height: 22px; }
  .scenario__title::after { content: ""; position: absolute; right: 0; top: -8px; border-left: 8px solid var(--corner-blue); border-top: 8px solid transparent; }
  .scenario table { width: 100%; border-collapse: collapse; font-family: "Lato", sans-serif; font-size: 8.5px; color: var(--text-strong); }
  .scenario th { font-weight: 700; text-align: center; line-height: 1.1; padding: 3px 2px; background: #fff; vertical-align: bottom; }
  .scenario td { height: 13px; text-align: center; border-top: 1px solid var(--grid); background: var(--row-tint); padding: 0 2px; }
  .scenario td.row-label { background: #fff; text-align: left; padding-left: 6px; width: 52px; }

  .disclaimer { position: absolute; left: 70px; width: 460px; top: 652px; text-align: center;
    font-family: "Lato", sans-serif; font-style: italic; font-size: 8.5px; line-height: 1.4; color: var(--text); }
</style>
</head>
<body>
<main class="spread">
  <section class="page page--left">
    <div class="photo photo--handshake" role="img" aria-label="Photo of two businessmen shaking hands over a tablet and charts"></div>
    <svg class="wave wave--top" viewBox="0 0 600 300" aria-hidden="true">
      <path d="M0 250 C160 205 340 260 600 212 L600 300 L0 300 Z" fill="var(--paper)"/>
      <path d="M0 250 C160 205 340 260 600 212" fill="none" stroke="var(--brand-blue)" stroke-width="3"/>
    </svg>

    <div class="body-copy">
      <p>Messrs. Hale, Moreno and Whitcombe founded Juniper Ridge in 2010. Their debut fund was a boutique venture capital fund. Juniper Ridge is building upon the success of its first fund with the launch of Fund II, a venture debt fund that invests in early to mid-stage companies and securities with preferred returns.</p>
      <p class="lead">Fund II pays its investors a 9% annual return on a monthly basis, and a preference of 1.25x on repayments made in 3 years or less. If the repayment is extended beyond 3 years, the investors will be paid a 12% annual return on a monthly basis, with a preference of 1.5x on repayment. The fund is obligated to liquidate its portfolio to repay investors within five years of the date of their investment.</p>
      <p>The minimum investment in Fund II is fifty thousand dollars ($50,000). The first three years of interest is paid from a reserve and liquidations within the fund's portfolio will be used to pay the preferential returns and remaining interest payments. Investors should note that a sale of any of the Fund's assets could pay the preferential returns before the 3-year maturity date, and such early repayment would terminate the Fund's obligation to make further interest payments.</p>
    </div>

    <div class="photo photo--cash" role="img" aria-label="Photo of a pile of hundred dollar bills"></div>

    <svg class="wave wave--bottom" viewBox="0 0 600 140" aria-hidden="true">
      <path d="M0 40 C200 -5 380 60 600 18 L600 140 L0 140 Z" fill="var(--brand-blue)"/>
    </svg>
    <div class="brand">
      <div class="brand__mark"><span class="brand__square"></span>Juniper Ridge Fund</div>
      <div class="brand__url">www.juniperridgefund.com</div>
    </div>
  </section>

  <section class="page page--right">
    <div class="photo photo--couple" role="img" aria-label="Photo of a smiling couple meeting with an advisor"></div>
    <div class="photo photo--estate" role="img" aria-label="Photo of a large estate home with a lawn"></div>
    <svg class="wave wave--top" viewBox="0 0 600 300" aria-hidden="true">
      <path d="M0 200 C180 130 360 210 600 150 L600 300 L0 300 Z" fill="var(--paper)"/>
      <path d="M0 200 C180 130 360 210 600 150" fill="none" stroke="var(--brand-blue)" stroke-width="3"/>
    </svg>

    <h1 class="pro-forma">PRO FORMA</h1>

    <div class="scenario scenario--two">
      <div class="scenario__title">Exit in Two Years</div>
      <table>
        <tr><th></th><th>Investment Amount</th><th>Interest Rate</th><th>Interest Received</th><th>Preference Rate</th><th>Preference Amount</th><th>Total Return</th><th>Return on Investment</th></tr>
        <tr><td class="row-label">Year 1</td><td>$100,000</td><td>9%</td><td>$9,000</td><td></td><td></td><td></td><td></td></tr>
        <tr><td class="row-label">Year 2</td><td></td><td>9%</td><td>$9,000</td><td>1.25</td><td>$125,000</td><td></td><td></td></tr>
        <tr><td class="row-label">Total:</td><td></td><td></td><td>$18,000</td><td></td><td>$125,000</td><td>$143,000</td><td>43%</td></tr>
      </table>
    </div>

    <div class="scenario scenario--four">
      <div class="scenario__title">Exit in Four Years</div>
      <table>
        <tr><th></th><th>Investment Amount</th><th>Interest Rate</th><th>Interest Received</th><th>Preference Rate</th><th>Preference Amount</th><th>Total Return</th><th>Return on Investment</th></tr>
        <tr><td class="row-label">Year 1</td><td>$100,000</td><td>9%</td><td>$9,000</td><td></td><td></td><td></td><td></td></tr>
        <tr><td class="row-label">Year 2</td><td></td><td>9%</td><td>$9,000</td><td></td><td></td><td></td><td></td></tr>
        <tr><td class="row-label">Year 3</td><td></td><td>9%</td><td>$9,000</td><td></td><td></td><td></td><td></td></tr>
        <tr><td class="row-label">Year 4</td><td></td><td>12%</td><td>$12,000</td><td>1.5</td><td>$150,000</td><td></td><td></td></tr>
        <tr><td class="row-label">Total:</td><td></td><td></td><td>$39,000</td><td></td><td>$150,000</td><td>$189,000</td><td>89%</td></tr>
      </table>
    </div>

    <div class="photo photo--boardroom" role="img" aria-label="Photo of an empty boardroom with leather chairs around a long table"></div>

    <p class="disclaimer">Please note that these are forward-looking statements by the Fund's management, which cannot be relied upon to accurately project actual future returns on an investment in the Fund (See Risk Factors in the Fund's PPM).</p>

    <svg class="wave wave--bottom" viewBox="0 0 600 140" aria-hidden="true">
      <path d="M0 110 C200 120 420 90 600 40 L600 140 L0 140 Z" fill="var(--brand-blue)"/>
    </svg>
  </section>
</main>
</body>
</html>
```